Brand new start up connecting advertisers to the gaming community needs a cool website design

The company is called Quenzly with the tagline "Gamers, Fans, and Brands". I connect the advertisers and their brands/services with sponsorship opportunities within the gaming community, which includes popular streamers, professional gamers and teams as well as venues that host popular events.

I need a website that's fun, eye-catching and playful but not at the expense of professionalism. I'm in the gaming space so some degree of playfulness within the site and context is desired.

As an example, I envision a plugin for the initial load screen where the letters of my logo (see uploaded files for visual) fall from the top of the screen upside down (hence the "quenzly") and bounce into place centered on the screen above the fold . Once that sequence concludes (a few seconds), it holds in place and then the letters turn into correct form to form the logo. After all that the tagline appears underneath. I think a 5 second total sequence of all this makes the most sense and it only loads when you initially visit.

I have other ideas but welcome yours. If you've worked in this esports/gaming environment before, I would love to hear your thoughts and suggestions. If you haven't, that's ok too.

Please keep in mind, I need to keep a professional tone throughout this project's design. Meridex 400 companies and the largest ad agencies in the world will be my clients. I need them to know that Quenzly is legit and credible not goofy and all "gamey"

Target Market(s)

it's two fold. The primary target will be adults 25-54 but a secondary target is streamers/gamers/video gaming community that is mostly male 12-34.

Industry/Entity Type

Advertising

Coding

Coded - Design and coding required

Number of Pages Required

4 page

Font styles to use
Sans Serif

Requirements
Must have
• A fun, playful website that is also professional.

I'm going to eventually drop in video examples of work I've done.

Cool backgrounds can either be developed or be from static pictures i own or use from large gaming tournaments showcasing the excitement around the experience.

Use whatever logo uploaded in the files that you think works best with your design
Nice to have
• Experiment with cool fonts as long as they are easy to read

Have fun with little "easter eggs" in the design such as things the visitors discovers when navigating the web page. Maybe when the cursor rolls over a letter in the logo, it reacts in a fun way such as inverting or expanding???

I'm open to anything fun as long as it doesn't dominate the experience. Playful should be limited to a few fun things but not be the epi-center of the experience.

If you want to explore other options or get better explanation on what this means, email me.
Should not have
• It shouldn't feel too business-like or static. I need a balance that leans professional with fun throughout that does NOT compromise the user's experience.

Do not play off of existing/traditional gaming clip art or proprietary trademarks like the velora symbol, Zentro logo, Moss Prowler monster, etc...

```html
<!DOCTYPE html>
<html lang="en">
<head>
<meta charset="utf-8">
<title>Quenzly — Gamers, Fans &amp; Brands</title>
<link href="https://fonts.googleapis.com/css2?family=Montserrat:wght@400;600;700;800&family=Open+Sans:wght@400;600;700&display=swap" rel="stylesheet">
<style>
  :root {
    --black: #000000;
    --ink: #0a0a0a;
    --green: #3ee62a;
    --green-deep: #2fd11c;
    --white: #ffffff;
    --muted: #cfcfcf;
    --purple: #4b2a8c;
    --violet: #7b4fd6;
  }
  * { margin: 0; padding: 0; box-sizing: border-box; }
  html, body { width: 1200px; height: 2288px; overflow: hidden; }
  body { background: var(--black); font-family: "Open Sans", Arial, sans-serif; color: var(--white); position: relative; }

  .page {
    position: absolute; left: 128px; top: 112px; width: 960px; height: 2068px;
    background: var(--ink);
    box-shadow: 0 0 28px 6px rgba(62,230,42,.55), 0 0 70px 14px rgba(62,230,42,.25);
    overflow: hidden;
  }

  /* header */
  .site-header { position: absolute; left: 0; top: 0; width: 960px; height: 68px; background: var(--black); }
  .brand { position: absolute; left: 64px; top: 12px; }
  .brand-name { font-family: "Montserrat", Arial, sans-serif; font-weight: 800; font-size: 26px; letter-spacing: 3px; color: var(--green); line-height: 1; }
  .brand-tagline { font-family: "Montserrat", Arial, sans-serif; font-size: 10px; letter-spacing: 2px; color: var(--white); margin-top: 4px; }
  .nav { position: absolute; right: 40px; top: 24px; display: flex; gap: 30px; font-size: 13px; }
  .nav a { color: var(--white); text-decoration: none; }
  .nav a.active { color: var(--green); }

  /* hero */
  .hero { position: absolute; left: 0; top: 68px; width: 960px; height: 460px; }
  .hero-media { position: absolute; inset: 0; background: radial-gradient(ellipse at 30% 70%, #3a6fb0 0%, transparent 40%), radial-gradient(ellipse at 75% 40%, var(--violet) 0%, transparent 55%), linear-gradient(135deg, #1b1036 0%, var(--purple) 50%, #160a2a 100%); }
  .hero-title { position: absolute; left: 64px; top: 106px; font-family: "Montserrat", Arial, sans-serif; font-weight: 700; font-size: 66px; color: var(--white); }
  .hero-sub { position: absolute; left: 64px; top: 200px; width: 580px; font-weight: 700; font-size: 22px; line-height: 1.4; color: var(--green); }
  .btn { display: inline-block; background: var(--green-deep); color: var(--white); font-size: 13px; font-weight: 600; padding: 9px 16px; border-radius: 2px; }
  .hero .btn { position: absolute; left: 64px; top: 300px; }

  /* sections */
  .section-title { font-family: "Montserrat", Arial, sans-serif; font-size: 28px; font-weight: 400; color: var(--white); display: flex; align-items: center; gap: 10px; }
  .section-title span { color: var(--green); }
  .section-title::after { content: ""; flex: 1; height: 2px; background: var(--green); }
  .copy { font-size: 12.5px; line-height: 1.85; color: var(--muted); }

  .about { position: absolute; left: 0; top: 528px; width: 960px; height: 600px; background: var(--black); }
  .about-text { position: absolute; left: 80px; top: 100px; width: 360px; }
  .about .section-title { width: 440px; }
  .about .copy { margin-top: 34px; }
  .about .btn { margin-top: 30px; }
  .about-media { position: absolute; left: 470px; top: 120px; width: 420px; height: 280px; background: radial-gradient(ellipse at 50% 60%, #1f3d1a 0%, #222 40%, #0c0c0c 80%); }

  .feature { position: absolute; left: 0; top: 1128px; width: 960px; height: 300px; }
  .feature-media { position: absolute; inset: 0; background: radial-gradient(ellipse at 70% 50%, #3b6fb5 0%, transparent 50%), linear-gradient(90deg, #1a2c55 0%, #2a4e8c 50%, #1a1f3a 100%); }
  .feature-play { position: absolute; left: 456px; top: 96px; }
  .feature-caption { position: absolute; left: 0; width: 960px; top: 160px; text-align: center; font-weight: 700; font-size: 20px; color: var(--white); }

  .services { position: absolute; left: 0; top: 1428px; width: 960px; height: 400px; background: var(--black); }
  .services-media { position: absolute; left: 92px; top: 60px; width: 340px; height: 280px; background: linear-gradient(135deg, #0e3a6b 0%, #1f6fb8 45%, #5a2a8c 100%); }
  .services-text { position: absolute; left: 470px; top: 56px; width: 420px; }
  .services .copy { margin-top: 26px; }
  .services .btn { margin-top: 24px; }

  /* footer */
  .site-footer { position: absolute; left: 0; top: 1828px; width: 960px; height: 240px; background: var(--green); }
  .social-list { position: absolute; left: 40px; top: 70px; width: 880px; display: flex; }
  .social-item { flex: 1; text-align: center; font-size: 11px; line-height: 1.45; color: var(--white); border-right: 1px solid rgba(255,255,255,.55); }
  .social-item:last-child { border-right: none; }
  .social-dot { display: block; width: 18px; height: 18px; border-radius: 50%; background: var(--white); margin: 0 auto 12px; }
  .copyright { position: absolute; left: 0; width: 960px; top: 205px; text-align: center; font-size: 9px; color: var(--white); }
</style>
</head>
<body>
<div class="page">
  <header class="site-header">
    <div class="brand">
      <div class="brand-name">QUENZLY</div>
      <div class="brand-tagline">Gamers, Fans &amp; Brands</div>
    </div>
    <nav class="nav">
      <a class="active" href="#">Home</a>
      <a href="#">How We Can Help</a>
      <a href="#">What we do</a>
      <a href="#">Merchandise</a>
      <a href="#">Contact Us</a>
    </nav>
  </header>

  <section class="hero">
    <div class="hero-media" role="img" aria-label="Gaming desk with backlit keyboard and mouse in purple light"></div>
    <h1 class="hero-title">Quenzly</h1>
    <p class="hero-sub">Neque porro quisquam est qui dolorem ipsum quia dolor sit amet, consectetur, adipisci velit</p>
    <span class="btn">Get started</span>
  </section>

  <section class="about">
    <div class="about-text">
      <h2 class="section-title">ABOUT <span>US</span></h2>
      <p class="copy">At vero eos et accusamus et iusto odio dignissimos ducimus qui blanditiis praesentium voluptatum deleniti atque corrupti quos dolores et quas molestias excepturi sint occaecati cupiditate non provident, similique sunt in culpa qui officia deserunt mollitia animi, id est laborum et dolorum fuga. Et harum quidem rerum facilis est et expedita distinctio. Nam libero tempore, cum soluta nobis est eligendi optio cumque nihil impedit quo minus id quod maxime placeat facere possimus, omnis voluptas assumenda est.</p>
      <span class="btn">Read More</span>
    </div>
    <div class="about-media" role="img" aria-label="Black game controller with green glowing light"></div>
  </section>

  <section class="feature">
    <div class="feature-media" role="img" aria-label="Players at a tournament with lit keyboards"></div>
    <svg class="feature-play" width="48" height="48" viewBox="0 0 48 48" aria-hidden="true">
      <circle cx="24" cy="24" r="24" fill="#2fd11c"/>
      <path d="M19 14 L35 24 L19 34 Z" fill="#ffffff"/>
    </svg>
    <p class="feature-caption">Neque porro quisquam est</p>
  </section>

  <section class="services">
    <div class="services-media" role="img" aria-label="Gamer playing at a multi-screen setup in blue light"></div>
    <div class="services-text">
      <h2 class="section-title">WHAT <span>WE DO</span></h2>
      <p class="copy">At vero eos et accusamus et iusto odio dignissimos ducimus qui blanditiis praesentium voluptatum deleniti atque corrupti quos dolores et quas molestias excepturi sint occaecati cupiditate non provident, similique sunt in culpa qui officia deserunt mollitia animi, id est laborum et dolorum fuga. Et harum quidem rerum facilis est et expedita distinctio.</p>
      <span class="btn">Read More</span>
    </div>
  </section>

  <footer class="site-footer">
    <ul class="social-list">
      <li class="social-item"><span class="social-dot"></span>Photoreel<br>Quenzly</li>
      <li class="social-item"><span class="social-dot"></span>Chirper<br>Quenzly</li>
      <li class="social-item"><span class="social-dot"></span>Circlebook<br>Quenzly</li>
      <li class="social-item"><span class="social-dot"></span>Workweb<br>Quenzly</li>
      <li class="social-item"><span class="social-dot"></span>Streamtube<br>Quenzly</li>
    </ul>
    <p class="copyright">Copyright © 2020 Quenzly Company Name. All Rights Reserved</p>
  </footer>
</div>
</body>
</html>
```